Fenwell Building Partners Stationary Revamp

We need a full set of new stationary including business cards for our Public Sector Construction company based in the South East of England. We have a new logo (attached) that we want to launch and revamp all of our company literature. We are required to send a lot of correspondence to residents etc so a consistent theme is required across everything. Also attached is our existing templates.

Target Market(s)

We work for Council and government provided housing organisations and NOT private individuals. All of our clients represent government spent money, so we need to look professional and instantly recognisable brand.

Industry/Entity Type

Business

Colors

Designer to choose colors to be used in the design.

Requirements
Must have
• New fresh designs that utilise our new logo. And the letterhead needs to be able to be rolled out onto a word template so that all staff can type straight onto it rather than us having to have it printed first.
Nice to have
• I am looking forward to seeing your best efforts as designers.

```html
<!DOCTYPE html>
<html lang="en">
<head>
<meta charset="utf-8">
<title>Fenwell Building Partners – Business Card</title>
<link rel="stylesheet" href="https://fonts.googleapis.com/css2?family=Open+Sans:wght@400;600;700&display=swap">
<style>
  :root {
    --backdrop: #3a3a3c;
    --card-dark: #1f1613;
    --card-black: #0d0d0e;
    --card-white: #f6f6f4;
    --gold: #e2b21c;
    --gold-deep: #c99a10;
    --ink: #1c1c1c;
    --light-text: #f1f1f1;
    --muted: #a9a9a9;
  }
  html, body {
    margin: 0;
    padding: 0;
    width: 1200px;
    height: 960px;
    overflow: hidden;
    background: var(--backdrop);
    font-family: "Open Sans", Arial, sans-serif;
  }
  .canvas {
    position: relative;
    width: 1200px;
    height: 960px;
  }
  .card {
    position: absolute;
    left: 250px;
    width: 700px;
    height: 400px;
    overflow: hidden;
    box-shadow: 0 10px 30px rgba(0,0,0,0.35);
  }
  .card-back { top: 50px; background: var(--card-black); }
  .card-front { top: 500px; background: var(--card-dark); }

  .card-back .brand {
    position: absolute;
    top: 150px;
    left: 0;
    width: 100%;
    text-align: center;
    color: var(--light-text);
    font-size: 34px;
    font-weight: 600;
    letter-spacing: 0.5px;
  }
  .card-back .brand-rule {
    position: absolute;
    top: 205px;
    left: 200px;
    width: 300px;
    height: 1px;
    background: var(--muted);
  }
  .card-back .web {
    position: absolute;
    top: 300px;
    width: 100%;
    text-align: center;
    color: var(--muted);
    font-size: 17px;
    letter-spacing: 3px;
  }

  .front-shape { position: absolute; inset: 0; }

  .contact {
    position: absolute;
    left: 40px;
    top: 36px;
    color: var(--light-text);
  }
  .contact .name {
    color: var(--gold);
    font-weight: 700;
    font-size: 21px;
    margin: 0;
  }
  .contact .role {
    font-size: 16px;
    margin: 2px 0 26px;
    letter-spacing: 0.3px;
  }
  .contact .address {
    font-size: 15px;
    line-height: 1.35;
    margin: 0 0 14px;
  }
  .contact ul {
    list-style: none;
    margin: 0 0 6px;
    padding: 0;
    font-size: 15px;
    line-height: 1.45;
  }
  .contact li { display: flex; align-items: center; gap: 9px; }
  .contact li svg { width: 13px; height: 13px; fill: var(--gold); flex: none; }
  .contact .reg { font-size: 15px; margin: 0; }

  .front-brand {
    position: absolute;
    left: 395px;
    top: 175px;
    width: 280px;
    display: flex;
    align-items: center;
    gap: 12px;
    color: var(--ink);
    font-size: 24px;
    font-weight: 600;
    line-height: 1.15;
  }
  .front-brand .dot {
    width: 22px;
    height: 22px;
    border-radius: 50%;
    background: var(--gold);
    flex: none;
  }
</style>
</head>
<body>
<main class="canvas">

  <section class="card card-back" aria-label="Business card back">
    <div class="brand">Fenwell Building Partners</div>
    <div class="brand-rule"></div>
    <div class="web">www.fenwellbp.co.uk</div>
  </section>

  <section class="card card-front" aria-label="Business card front">
    <svg class="front-shape" width="700" height="400" viewBox="0 0 700 400" aria-hidden="true">
      <path d="M330 0 C 260 90, 240 260, 365 400 L700 400 L700 0 Z" fill="var(--gold)"/>
      <path d="M345 0 C 282 95, 268 255, 392 400 L700 400 L700 0 Z" fill="var(--card-white)"/>
    </svg>

    <div class="contact">
      <p class="name">R J HARTLEY MIOD</p>
      <p class="role">MANAGING DIRECTOR</p>
      <p class="address">Marlow House<br>12 Kestrel Lane<br>Ashford, Kent, TN23 4QP</p>
      <ul>
        <li>
          <svg viewBox="0 0 16 16"><path d="M3 1 L6 1 L7 5 L5 6.5 C6 9 7 10 9.5 11 L11 9 L15 10 L15 13 C15 14 14 15 13 15 C6 15 1 10 1 3 C1 2 2 1 3 1 Z"/></svg>
          020 7946 0312
        </li>
        <li>
          <svg viewBox="0 0 16 16"><rect x="1" y="6" width="14" height="8" rx="1"/><rect x="4" y="1" width="8" height="4"/></svg>
          020 7946 0318
        </li>
        <li>
          <svg viewBox="0 0 16 16"><path d="M1 3 H15 V13 H1 Z M1 3 L8 9 L15 3" stroke="#1f1613" stroke-width="1"/></svg>
          info@fenwellbp.co.uk
        </li>
        <li>
          <svg viewBox="0 0 16 16"><circle cx="8" cy="8" r="7"/></svg>
          www.fenwellbp.co.uk
        </li>
      </ul>
      <p class="reg">Reg No: 07316248</p>
    </div>

    <div class="front-brand">
      <span class="dot"></span>
      <span>Fenwell Building Partners</span>
    </div>
  </section>

</main>
</body>
</html>
```